Banner Ad Needed For Real Estate Lending Firm

We are taking out a banner ad on one of the most highly trafficked real estate websites in New York. The ad will be 970x250. Display format will be JPEG or animated GIF, but original art files will be required as well from the winning designer.

Granite Path Lending (or GPL) is one of the largest "hard money lenders" for real estate investors on the East Coast of the US. We lend for the following real estate investments: 1) Fix And Flip 2) New Construction 3) Cash Out Refinance. We close in 2-10 days. More information can be found on our website here: http://www.gpl7.example/

Our goal is to help small business owners, real estate investors, and commercial contractors quickly and efficiently finance their business activities. Our local hard money loan programs are tailored to your unique project needs. We fund fix and flip, new construction, and cash out refinance projects for non-owner occupied properties.

Target Market(s)

Real Estate Agents, Real Estate Investors, Mortgage Brokers, Other Real Estate Professionals

Industry/Entity Type

Real Estate

Font styles to use
Sans Serif

Requirements
Must have
• Must incorporate the fact that we close deals very fast (2 - 10 days), finance the following these 2 main types of investments (Fix and Flip, New Construction), and mention that Brokers can make up to 2.5 Points.
• See attached style guide for basic colors and fonts.
Nice to have
• Animated GIF might be a great feature!

```html
<!DOCTYPE html>
<html lang="en">
<head>
<meta charset="utf-8">
<title>Granite Path Lending – Banner Set</title>
<link rel="stylesheet" href="https://fonts.googleapis.com/css2?family=Figtree:wght@500;600&family=Roboto+Slab:wght@300;400&display=swap">
<style>
  :root {
    --page-bg: #ffffff;
    --panel-dark: #0d4f5e;
    --band-deep: #0a3e4b;
    --band-sage: #4f8a7d;
    --stripe: #4f8a7d;
    --button: #1793b0;
    --note-bg: #0a3e4b;
    --text-light: #ffffff;
    --text-soft: #e6eef0;
  }
  * { margin: 0; padding: 0; box-sizing: border-box; }
  html, body {
    width: 1200px; height: 1129px; overflow: hidden;
    background: var(--page-bg);
  }
  .canvas { position: relative; width: 1200px; height: 1129px; }
  .banner-slot {
    position: absolute; left: 51px;
    width: 1109px; height: 286px; overflow: hidden;
  }
  .banner-slot--first { top: 89px; }
  .banner-slot--second { top: 427px; }
  .banner-slot--third { top: 766px; }
  .banner {
    position: absolute; left: 0; top: 0;
    width: 970px; height: 250px;
    transform: scale(1.1433); transform-origin: 0 0;
    overflow: hidden;
  }
  .banner__photo { position: absolute; left: 455px; top: 0; width: 515px; height: 250px; }
  .banner__photo--skyline { background: linear-gradient(180deg, #3f5f9c 0%, #8a7d86 35%, #b0743a 62%, #6e4320 100%); }
  .banner__photo--crew { background: linear-gradient(135deg, #4a3a2c 0%, #9a9791 30%, #b9b6ae 60%, #8d8a84 100%); }
  .banner__photo--team { background: linear-gradient(135deg, #6a4a3c 0%, #8e5a44 35%, #7b7a78 65%, #a9a6a0 100%); }
  .banner__shapes { position: absolute; left: 0; top: 0; width: 970px; height: 250px; }
  .brand {
    position: absolute; left: 24px; top: 9px;
    display: flex; align-items: center; gap: 36px;
    font-family: "Figtree", sans-serif; font-weight: 600;
    font-size: 16.5px; line-height: 22px; letter-spacing: 0.2px;
    color: var(--text-soft); text-transform: uppercase;
  }
  .brand__square { width: 60px; height: 60px; background: var(--text-soft); }
  .headline {
    position: absolute; left: 13px; top: 88px;
    font-family: "Figtree", sans-serif; font-weight: 600;
    font-size: 38.5px; line-height: 43px; color: var(--text-light);
    letter-spacing: -0.3px; white-space: nowrap;
  }
  .summary {
    position: absolute; left: 17px; top: 187px;
    font-family: "Roboto Slab", serif; font-weight: 300;
    font-size: 16.5px; line-height: 26px; color: var(--text-soft);
    white-space: nowrap;
  }
  .cta {
    position: absolute; left: 706px; top: 102px;
    width: 242px; height: 60px;
    display: flex; align-items: center; justify-content: center;
    background: var(--button); color: var(--text-light);
    font-family: "Figtree", sans-serif; font-weight: 500; font-size: 18px;
  }
  .offer-note {
    position: absolute; left: 706px; top: 168px;
    width: 242px; padding: 6px 8px;
    background: var(--note-bg); color: var(--text-light);
    font-family: "Figtree", sans-serif; font-weight: 500;
    font-size: 12.5px; line-height: 17px; text-align: center;
  }
</style>
</head>
<body>
<main class="canvas">

  <section class="banner-slot banner-slot--first">
    <div class="banner">
      <div class="banner__photo banner__photo--skyline" role="img" aria-label="Photo of a city construction site with tower cranes at dusk"></div>
      <svg class="banner__shapes" viewBox="0 0 970 250" aria-hidden="true">
        <polygon points="0,0 500,0 460,250 0,250" fill="var(--panel-dark)"/>
        <polygon points="500,0 526,0 486,250 460,250" fill="var(--stripe)"/>
        <polygon points="0,79 487,79 470,184 0,184" fill="var(--band-sage)"/>
      </svg>
      <div class="brand"><span class="brand__square"></span><span>Granite<br>Path<br>Lending LLC</span></div>
      <h1 class="headline">Your Fastest Local Source<br>for Hard Money</h1>
      <p class="summary">We fund fix and flip, new construction, and cash out<br>refinance projects for non-owner occupied properties.</p>
      <div class="cta">Pre-Qualify Today</div>
      <p class="offer-note">We close in 2–10 days<br>Brokers earn up to 2.5 points</p>
    </div>
  </section>

  <section class="banner-slot banner-slot--second">
    <div class="banner">
      <div class="banner__photo banner__photo--crew" role="img" aria-label="Overhead photo of workers in hard hats laying rebar and concrete"></div>
      <svg class="banner__shapes" viewBox="0 0 970 250" aria-hidden="true">
        <polygon points="0,0 500,0 460,250 0,250" fill="var(--panel-dark)"/>
        <polygon points="500,0 526,0 486,250 460,250" fill="var(--stripe)"/>
        <polygon points="0,79 487,79 470,184 0,184" fill="var(--band-deep)"/>
      </svg>
      <div class="brand"><span class="brand__square"></span><span>Granite<br>Path<br>Lending LLC</span></div>
      <h2 class="headline">Your Fastest Local Source<br>for Hard Money</h2>
      <p class="summary">We fund fix and flip, new construction, and cash out<br>refinance projects for non-owner occupied properties.</p>
      <div class="cta">Pre-Qualify Today</div>
      <p class="offer-note">We close in 2–10 days<br>Brokers earn up to 2.5 points</p>
    </div>
  </section>

  <section class="banner-slot banner-slot--third">
    <div class="banner">
      <div class="banner__photo banner__photo--team" role="img" aria-label="Photo of two builders kneeling on a rooftop work site"></div>
      <svg class="banner__shapes" viewBox="0 0 970 250" aria-hidden="true">
        <polygon points="0,0 500,0 460,250 0,250" fill="var(--panel-dark)"/>
        <polygon points="500,0 526,0 486,250 460,250" fill="var(--stripe)"/>
        <polygon points="0,79 487,79 470,184 0,184" fill="var(--band-deep)"/>
      </svg>
      <div class="brand"><span class="brand__square"></span><span>Granite<br>Path<br>Lending LLC</span></div>
      <h2 class="headline">Your Fastest Local Source<br>for Hard Money</h2>
      <p class="summary">We fund fix and flip, new construction, and cash out<br>refinance projects for non-owner occupied properties.</p>
      <div class="cta">Pre-Qualify Today</div>
      <p class="offer-note">We close in 2–10 days<br>Brokers earn up to 2.5 points</p>
    </div>
  </section>

</main>
</body>
</html>
```